Design of a Web Development Agency

We're a web development agency (we do not offer design services). We'd like to get a new website up and running. We do custom web application development - large scale applications in the financial, healthcare, automotive, and other industries.

We need the following types of pages designed:
1) Homepage
2) Blog
3) Services page
4) Packages page
4) Generic content
5) Contact Us form.

The design should be consistent with our current icon. We're looking for a clean, corporate, brand. We'd like the design to expand on the concepts in the logo - the use of the electrical wiring motif / the colors / etc.

We offer the following services: 1) Cobalto web hosting consulting, 2) custom application development, 3) Qel development, 4) Veltrix development.

We offer packages in numbers of hours. We have about 3-4 tiers of services - the number of hours versus the monthly invoice total. For example, 5 hours per month of $500.00, for example.

Target Market(s)

Corporate clients

Industry/Entity Type

Electrical

Colors
acd036
33b7a4
33a6d7
3176b5
876aae
b768aa
fbee3e

Requirements
Must have
• Responsive / mobile friendly design.
• An email submitting form on the contact us page
Nice to have
• We'd like a bit of San Francisco to come through (where we're located)
• A plorvo map of our address on the contact us page
Should not have
• Excessive imagery. We don't have a lot of imagery, so we'd basically have to go out and find stock photography to put in it's place, which we just don't really want to do. All imagery should be supplied by the designer (we'll pay any copyright fees, if applicable, you just have to send us a list of the links to the imagery. Max budget would be $100-$200 on imagery, but preferably as little as possible).

```html
<!DOCTYPE html>
<html lang="en">
<head>
<meta charset="utf-8">
<title>Halden Web Works</title>
<link href="https://fonts.googleapis.com/css2?family=Open+Sans:wght@300;400&display=swap" rel="stylesheet">
<style>
:root{
  --topbar:#5b5b5b;
  --dark:#353535;
  --card:#333333;
  --olive:#87961a;
  --olive-dark:#6b7812;
  --gold:#f2b300;
  --text:#555555;
  --heading:#333333;
  --muted:#9a9a9a;
  --white:#ffffff;
}
*{margin:0;padding:0;box-sizing:border-box}
html,body{width:939px;height:1200px;overflow:hidden;background:var(--white)}
body{position:relative;font-family:Arial,Helvetica,sans-serif;color:var(--text)}
.abs{position:absolute}
.light{font-family:'Open Sans',sans-serif;font-weight:300}

.topbar{left:0;top:0;width:939px;height:29px;background:var(--topbar);color:#eee;font-size:8px}
.topbar .call{left:137px;top:8px;display:flex;align-items:center;gap:5px}
.topbar .social{right:136px;top:9px;display:flex;align-items:center;gap:14px;font-style:italic;font-size:7px}
.topbar .dot{width:7px;height:7px;border-radius:50%;background:#ddd}

.header{left:0;top:29px;width:939px;height:61px;background:var(--white)}
.brand{left:137px;top:38px;display:flex;align-items:center;gap:8px;font-family:'Open Sans',sans-serif;font-size:12px;color:#222}
.brand .mark{width:42px;height:42px;border-radius:50%;border:2px solid #333;background:#c9d62c}
.nav{left:366px;top:55px;display:flex;gap:0;font-size:9.5px;color:#555}
.nav span{margin-right:47px}

.hero{left:0;top:90px;width:939px;height:534px;background:radial-gradient(ellipse at 25% 15%,#6a6a6a 0%,#2b2b2b 35%,#1c1c1c 60%),linear-gradient(#222,#111)}
.hero .bridge{left:0;top:0;width:939px;height:534px;background:linear-gradient(110deg,transparent 35%,rgba(200,110,20,.55) 45%,rgba(150,80,10,.35) 55%,transparent 70%),linear-gradient(180deg,transparent 55%,rgba(220,150,40,.25) 70%,transparent 85%)}
.hero h1{left:462px;top:150px;font-size:35px;color:var(--white);white-space:nowrap}
.hero h2{left:462px;top:193px;font-size:23px;color:var(--gold);white-space:nowrap}
.arrow{top:230px}

.service{background:var(--card);border-top:5px solid var(--olive);text-align:center;padding-top:20px}
.service h3{font-family:'Open Sans',sans-serif;font-weight:400;font-size:14px;line-height:18px;color:var(--gold)}
.service p{font-size:8px;line-height:16px;color:var(--muted);margin-top:10px}
.service .ring{width:70px;height:70px;border-radius:50%;border:2px solid var(--gold);margin:0 auto 12px;display:flex;align-items:center;justify-content:center}
.service .ring i{width:34px;height:26px;border-radius:50%;background:var(--gold)}

.packages{left:0;top:624px;width:939px;height:77px;background:var(--dark)}
.packages h4{left:134px;top:11px;font-size:19px;color:var(--gold)}
.packages p{left:135px;top:41px;font-size:13px;color:#999;font-family:'Open Sans',sans-serif}
.btn{background:var(--olive);border-bottom:3px solid var(--olive-dark);color:var(--white);font-family:'Open Sans',sans-serif;display:flex;align-items:center;justify-content:center}

.intro h2{left:0;width:939px;top:745px;text-align:center;font-size:26px;color:var(--heading)}
.intro p{left:0;width:939px;top:790px;text-align:center;font-size:11px;color:#555}

.screen{left:138px;top:854px;width:281px;height:189px;background:#111;border-radius:6px;padding:11px 13px}
.screen div{width:100%;height:100%;background:linear-gradient(135deg,#dfe6ea,#8d9aa3 60%,#3a3f44)}
.stand{left:248px;top:1043px;width:62px;height:46px;background:linear-gradient(#ccc,#888);clip-path:polygon(10% 0,90% 0,100% 100%,0 100%)}
.shadow{left:188px;top:1086px;width:180px;height:8px;border-radius:50%;background:radial-gradient(#bbb,transparent 70%)}

.about h2{left:479px;top:851px;font-size:26px;color:var(--heading)}
.about p{left:480px;top:895px;width:320px;font-size:9.5px;line-height:18.2px;color:#555}
.address{left:480px;top:1000px;display:flex;gap:10px;font-size:11px;line-height:18px;color:var(--olive)}

.footer{left:0;top:1134px;width:939px;height:66px;background:var(--dark);font-size:8px;color:#ccc}
.footer .links{left:137px;top:29px;display:flex}
.footer .links span{margin-right:27px}
.footer .copy{right:134px;top:29px}
</style>
</head>
<body>

<div class="abs topbar">
  <div class="abs call">
    <svg width="14" height="14" viewBox="0 0 14 14"><circle cx="7" cy="7" r="6" fill="none" stroke="#eee" stroke-width="1"/><path d="M4.5 4c.5-.5 1-.5 1.3 0l.6 1c.2.4 0 .7-.3 1 .4.8 1 1.4 1.8 1.8.3-.3.6-.5 1-.3l1 .6c.5.3.5.8 0 1.3-.8.8-2 .6-3.3-.4S4 6.2 4 5.2c0-.5.2-.9.5-1.2z" fill="#eee"/></svg>
    Call Us : (415) 555-0142
  </div>
  <div class="abs social">Connect with our social network : <i class="dot"></i><i class="dot"></i><i class="dot"></i><i class="dot"></i><i class="dot"></i><i class="dot"></i></div>
</div>

<div class="abs header"></div>
<div class="abs brand"><i class="mark"></i>HALDEN WEB WORKS</div>
<nav class="abs nav"><span>Home</span><span>About us</span><span>Blog</span><span>Services</span><span>Packages</span><span>Contact us</span></nav>

<section class="abs hero">
  <div class="abs bridge" role="img" aria-label="Night photograph of a San Francisco suspension bridge lit in orange over the bay"></div>
  <h1 class="abs light">Building a cloud application</h1>
  <h2 class="abs light">so solid, you can't fall through it</h2>
  <svg class="abs arrow" style="left:62px" width="16" height="62" viewBox="0 0 16 62"><path d="M14 2L2 31l12 29" fill="none" stroke="#777" stroke-width="1.5"/></svg>
  <svg class="abs arrow" style="left:874px" width="16" height="62" viewBox="0 0 16 62"><path d="M2 2l12 29L2 60" fill="none" stroke="#777" stroke-width="1.5"/></svg>
</section>

<div class="abs service" style="left:134px;top:419px;width:163px;height:191px;padding-top:18px">
  <div class="ring"><i></i></div>
  <h3>Cobalto web hosting<br>consulting</h3>
  <p>It is a long established fact that<br>a reader will be distracted...</p>
</div>
<div class="abs service" style="left:303px;top:500px;width:163px;height:110px">
  <h3>Custom application<br>development</h3>
  <p>It is a long established fact that<br>a reader will be distracted...</p>
</div>
<div class="abs service" style="left:473px;top:500px;width:162px;height:110px">
  <h3>Qel<br>Development</h3>
  <p>It is a long established fact that<br>a reader will be distracted...</p>
</div>
<div class="abs service" style="left:643px;top:500px;width:163px;height:110px">
  <h3>Veltrix<br>development</h3>
  <p>It is a long established fact that<br>a reader will be distracted...</p>
</div>

<section class="abs packages">
  <h4 class="abs light">Packages</h4>
  <p class="abs">We offer monthly retainers for our clients, providing different levels of service.</p>
  <div class="abs btn" style="left:625px;top:19px;width:181px;height:40px;font-size:15px">View Packages</div>
</section>

<section class="intro">
  <h2 class="abs light">We are &nbsp;a web development agency</h2>
  <p class="abs">We have helped dozens of clients migrate their data and web solutions to Norvane Cobalto's powerful cloud computing platform.</p>
</section>

<div class="abs screen"><div role="img" aria-label="Photograph of two colleagues working at a laptop in a bright office"></div></div>
<div class="abs stand"></div>
<div class="abs shadow"></div>

<section class="about">
  <h2 class="abs light">About Halden Web works</h2>
  <p class="abs">We have over 10 years of experience in architecting and implementing full-scale web applications from the financial, healthcare, automotive, and retail industries. From building social networking sites, inventory management, to reporting services, we can help you build out the tools to empower your business to grow and succeed.</p>
  <div class="abs address">
    <svg width="16" height="22" viewBox="0 0 16 22"><path d="M8 1a7 7 0 0 0-7 7c0 5 7 13 7 13s7-8 7-13a7 7 0 0 0-7-7z" fill="#87961a"/><circle cx="8" cy="8" r="3" fill="#fff"/></svg>
    <div>Address: 2750 Larkin Row, Suite 310,<br>San Francisco, CA 94109</div>
  </div>
  <div class="abs btn" style="left:480px;top:1053px;width:114px;height:37px;font-size:12px">Read More</div>
</section>

<footer class="abs footer">
  <div class="abs links"><span>Home</span><span>About us</span><span>Blog</span><span>Services</span><span>Packages</span><span>Contact us</span></div>
  <div class="abs copy">Copyrights 2014. Halden Web works. All rights reserved.</div>
</footer>

</body>
</html>
```